Design a website for our "Bright Stride" Initiative we are implementing at our Youth Soccer Club.

We need a web design for a wellness initiative for our soccer club. "Bright Stride" is the program title. The website will have health and wellness content related to our initiative. It should have interactive features for our users. Videos, survey/data submission capabilities, etc. Colors themed to align with logo. see my start of a website at www.brightstridewithtown.example. I like the homepage design, the rest is unprofessional looking. Design should provide education, tips, advice, resources, for health & wellness; wellness related to our pillars. 6 tabs in addition to home page: Drink more water, fuel your performance, stretch more, protect your skin more, move more, and sports mindset. (year 2 diagram wheel). Sports counseling will be next big focus. Wordpress based website. Easy for me to update in the future.

Target Market(s)

Families with children participating in soccer. concept also applicable to other youth sports.

Industry/Entity Type

Health And Wellness

Number of Pages Required

5+ page

Font styles to use
Sans Serif

Colors
0292cd
f37122

Requirements
Must have
• Bright Stride Logo
• Marrowby Field Soccer Club Logo (*updated*)
• Home page
• Video included that is currently on the website homepage www.brightstridewithtown.example
• Page for each of the 6 pillars
• Focus on "drink more water" pillar and "Mindset" (will focus on sports counseling)
• Flexibility for me to update/edit the website moving forward (non-coding).
• User friendly graphic/picture interface
Nice to have
• Design focused more on the themes, not on soccer. Want the design to be applicable to parents and youth of all sports. Education and interactive features to all ages.

```html
<!DOCTYPE html>
<html lang="en">
<head>
<meta charset="utf-8">
<title>Bright Stride</title>
<link rel="stylesheet" href="https://fonts.googleapis.com/css2?family=Open+Sans:wght@400;600;700&display=swap">
<style>
:root{
  --blue:#0292cd;
  --blue-dark:#0278ad;
  --orange:#f37122;
  --ink:#333333;
  --muted:#666666;
  --line:#d9d9d9;
  --dark:#1e1e1e;
  --light:#f5f5f5;
  --footer:#eeeeee;
}
*{box-sizing:border-box;margin:0;padding:0}
html,body{width:1200px;height:3072px;overflow:hidden}
body{font-family:"Open Sans",Arial,sans-serif;color:var(--ink);background:#fff;position:relative}
.wrap{width:934px;margin:0 auto;position:relative}
.section-title{color:var(--orange);font-size:23px;font-weight:600;text-align:center;text-transform:uppercase;letter-spacing:.5px}

/* hero */
.hero{height:553px;position:relative;background:linear-gradient(180deg,#15171c 0%,#2a2e33 45%,#5a5a3a 80%,#8a8a30 100%)}
.brand{position:absolute;top:48px;left:0;right:0;text-align:center}
.brand-dot{display:block;width:58px;height:58px;border-radius:50%;background:var(--orange);margin:0 auto 10px}
.brand-name{color:#27a1a8;font-size:20px;font-weight:700;letter-spacing:1px;text-transform:uppercase}
.play{position:absolute;left:579px;top:259px}
.hero-arrow{position:absolute;top:268px}
.hero-arrow.left{left:22px}.hero-arrow.right{right:22px}

/* nav */
.main-nav{height:61px;background:var(--blue)}
.main-nav ul{list-style:none;display:flex;height:61px;width:934px;margin:0 auto}
.main-nav li{color:#fff;font-size:11px;line-height:13px;padding:11px 10px 0;border-right:1px solid rgba(255,255,255,.25)}
.main-nav li:first-child{border-left:1px solid rgba(255,255,255,.25)}
.main-nav li.active{background:var(--blue-dark);font-weight:600;padding-top:19px}

/* welcome */
.welcome{padding-top:32px;height:451px}
.welcome p{font-size:11.5px;line-height:21px;color:var(--muted);text-align:center;margin-top:20px}
.pillars{display:flex;justify-content:space-between;margin-top:16px}
.pillar{width:149px;height:152px;border:1px solid var(--line);text-align:center;padding-top:26px;color:var(--blue);font-size:16px;line-height:20px}
.pillar svg{display:block;margin:0 auto 10px}

/* counseling */
.counsel{height:440px;background:linear-gradient(180deg,#4a4a4a,#2a2a2a)}
.counsel .section-title{color:#fff;padding-top:72px}
.cards{display:flex;justify-content:space-between;margin-top:22px}
.card{width:297px}
.card .photo{height:209px}
.card h3{color:var(--orange);font-size:19px;font-weight:600;text-align:center;margin-top:12px;text-transform:uppercase}

/* first steps */
.steps{height:314px;padding-top:70px}
.step-list{display:flex;justify-content:space-between;margin-top:28px}
.step{width:448px;display:flex;gap:16px}
.step-num{flex:none;width:36px;height:36px;background:var(--blue);color:#fff;font-size:20px;font-weight:600;display:flex;align-items:center;justify-content:center}
.step p{font-size:11px;line-height:22px;color:var(--muted)}

/* stats */
.stats{height:198px;background:linear-gradient(90deg,#2b2b2b,#1b1b1b 50%,#2b2b2b)}
.stat-row{display:flex;justify-content:space-around;padding:62px 40px 0}
.stat{text-align:center;color:#fff}
.stat b{display:block;font-size:40px;font-weight:700;line-height:44px}
.stat span{font-size:12px}

/* features */
.features{height:420px;padding-top:80px}
.feature h3{font-size:19px;line-height:23px}

/* testimonials */
.testimonials{height:399px;background:var(--light);padding-top:82px}
.avatars{display:flex;justify-content:center;align-items:center;gap:16px;margin-top:14px}
.avatar{width:76px;height:76px;border-radius:50%;background:linear-gradient(180deg,#bdbdbd,#8a8a8a);border:3px solid #fff}
.avatars .chev{margin:0 20px}
.quote{position:relative;width:760px;margin:24px auto 0;text-align:center;font-size:11px;line-height:21px;color:var(--muted);padding:0 70px}
.quote .mark{position:absolute;top:-2px;font-size:64px;line-height:60px;color:#c8c8c8;font-weight:700}
.quote .mark.open{left:-20px}.quote .mark.close{right:-20px}
.quote cite{display:block;font-style:normal;color:var(--ink);margin-top:10px;font-size:11.5px}

/* footer */
.site-footer{height:174px;background:var(--footer);padding-top:42px}
.footer-grid{display:flex}
.footer-links{list-style:none;font-size:11px;color:var(--muted);line-height:24px;width:135px}
.footer-links:nth-child(3){width:165px}
.footer-links li::before{content:"\2022";margin-right:6px;font-size:9px}
.newsletter{margin-left:15px;width:320px}
.newsletter h4,.social h4{font-size:13px;font-weight:600;margin-bottom:10px}
.subscribe{display:flex;height:40px}
.subscribe .field{width:217px;border:1px solid var(--line);background:#fff;font-size:11px;color:#aaa;padding:12px 16px}
.subscribe .btn{width:96px;background:#333;color:#fff;font-size:12px;display:flex;align-items:center;justify-content:center}
.social{margin-left:auto;width:80px}
.social-dots{display:grid;grid-template-columns:repeat(2,24px);gap:6px}
.social-dots i{width:24px;height:24px;border-radius:50%;background:var(--blue)}
.copyright{height:62px;background:var(--footer);border-top:1px solid var(--line);text-align:center;font-size:12px;line-height:60px}
</style>
</head>
<body>

<header class="hero" role="img" aria-label="Photo of young players in yellow kits listening to their coach at night">
  <div class="brand">
    <span class="brand-dot"></span>
    <span class="brand-name">Bright Stride</span>
  </div>
  <svg class="hero-arrow left" width="14" height="24" viewBox="0 0 14 24"><path d="M12 2 2 12l10 10" fill="none" stroke="rgba(255,255,255,.5)" stroke-width="2"/></svg>
  <svg class="hero-arrow right" width="14" height="24" viewBox="0 0 14 24"><path d="M2 2l10 10L2 22" fill="none" stroke="rgba(255,255,255,.5)" stroke-width="2"/></svg>
  <svg class="play" width="42" height="42" viewBox="0 0 42 42"><circle cx="21" cy="21" r="21" fill="#fff"/><path d="M16 12l14 9-14 9z" fill="#111"/></svg>
</header>

<nav class="main-nav">
  <ul>
    <li class="active">Home</li>
    <li>Water</li>
    <li>Fruits &amp;<br>Vegetables</li>
    <li>Stretch</li>
    <li>Fuel<br>Your Body</li>
    <li>Drink<br>More Water</li>
    <li>Fuel<br>Your Performance</li>
    <li>Stretch More</li>
    <li>Protect Your<br>Skin More</li>
    <li>Move More</li>
    <li>Sports Mindset</li>
  </ul>
</nav>

<section class="welcome wrap">
  <h2 class="section-title">Welcome to Bright Stride</h2>
  <p>Bright Stride is a partnership between Marrowby Field Soccer Club and the Northgate Foundation. It is an initiative to help communities develop attitudes and skills to make consistent and positive health-related choices. Promote healthy child development through involvement in sports, building a sense of well-being and meeting the growth, development, and activity needs of healthy, confident children and young people. A health and wellness initiative that will educate and provide resources to the players and their families in Marrowby Field Soccer Club.</p>
  <div class="pillars">
    <div class="pillar"><svg width="40" height="48" viewBox="0 0 40 48" fill="none" stroke="#0292cd" stroke-width="2.5"><rect x="15" y="2" width="10" height="6"/><path d="M13 8h14l3 6v32H10V14z"/><path d="M10 24h20M10 34h20"/></svg>Drink more<br>water</div>
    <div class="pillar"><svg width="40" height="48" viewBox="0 0 40 48"><path d="M20 14c-6-4-16-2-16 10 0 12 8 22 16 20 8 2 16-8 16-20 0-12-10-14-16-10z" fill="#0292cd"/><path d="M20 14c0-6 4-10 8-11" fill="none" stroke="#0292cd" stroke-width="2.5"/></svg>Fuel your<br>body</div>
    <div class="pillar"><svg width="40" height="48" viewBox="0 0 40 48" fill="none" stroke="#0292cd" stroke-width="3" stroke-linecap="round"><path d="M8 44C10 30 18 16 32 6"/><path d="M32 6l-8 2M32 6l-1 8"/></svg>Stretch more</div>
    <div class="pillar"><svg width="44" height="48" viewBox="0 0 44 48"><path d="M6 30c0-12 8-20 18-20s16 8 16 18z" fill="#0292cd"/><path d="M2 32h30" stroke="#0292cd" stroke-width="5" stroke-linecap="round"/></svg>Protect your<br>skin</div>
    <div class="pillar"><svg width="44" height="48" viewBox="0 0 44 48" fill="none" stroke="#0292cd" stroke-width="3" stroke-linecap="round"><path d="M4 24h30M26 14l10 10-10 10"/></svg>Move more</div>
    <div class="pillar"><svg width="44" height="48" viewBox="0 0 44 48" fill="none" stroke="#0292cd" stroke-width="2.5"><circle cx="22" cy="24" r="18"/><circle cx="22" cy="24" r="11"/><circle cx="22" cy="24" r="4" fill="#0292cd"/></svg>Sports<br>mindset</div>
  </div>
</section>

<section class="counsel" role="img" aria-label="Blurred photo of a sports field as section background">
  <div class="wrap">
    <h2 class="section-title">Sports Counseling/Psychology Ideas:</h2>
    <div class="cards">
      <div class="card"><div class="photo" role="img" aria-label="Photo of a family kicking a ball outdoors" style="background:linear-gradient(180deg,#5fa9b8,#6e8a4a)"></div><h3>For Parents</h3></div>
      <div class="card"><div class="photo" role="img" aria-label="Photo of a smiling tennis player holding a racket" style="background:linear-gradient(180deg,#9a8a3a,#d96a2c)"></div><h3>For Players</h3></div>
      <div class="card"><div class="photo" role="img" aria-label="Photo of a baseball coach talking with a young player" style="background:linear-gradient(180deg,#8aa868,#b04040)"></div><h3>For Coaches</h3></div>
    </div>
  </div>
</section>

<section class="steps wrap">
  <h2 class="section-title">First Steps</h2>
  <div class="step-list">
    <div class="step"><span class="step-num">1</span><p>I could come in and just do a simple discussion, presentation, or informational talk with the coaches during a coaches meeting. That way I could just make them aware of my services and how it might benefit their teams and players. Then coaches could just contact me on their own as they need.</p></div>
    <div class="step"><span class="step-num">2</span><p>I could conduct a presentation for parents. Could discuss the signs, symptoms of clinical issues and the impact on players. Could also discuss how parental responses and other external aspects (i.e.,...pressure at school, pressure from parents, coaches) impact player performance and sport enjoyment. Could also make parents aware of my services so that they could refer or contact me as needed.</p></div>
  </div>
</section>

<section class="stats" role="img" aria-label="Dark photo collage of young athletes in different sports">
  <div class="stat-row">
    <div class="stat"><b>65,432</b><span>Donec nisi dolor, egestas</span></div>
    <div class="stat"><b>523</b><span>Pellentesque egestas</span></div>
    <div class="stat"><b>97%</b><span>Aenean fermentum odio</span></div>
    <div class="stat"><b>1,558</b><span>Curabitur non diam</span></div>
  </div>
</section>

<section class="features wrap">
  <div class="cards">
    <div class="card feature"><div class="photo" role="img" aria-label="Photo of a boy drinking orange juice at a table" style="background:linear-gradient(180deg,#7a5a3a,#e09a40)"></div><h3>Performance and<br>Hydration</h3></div>
    <div class="card feature"><div class="photo" role="img" aria-label="Photo of colourful fresh vegetables" style="background:linear-gradient(180deg,#f4f4f0,#6aa040 60%,#d84030)"></div><h3>Boost Performance by<br>Adding Color</h3></div>
    <div class="card feature"><div class="photo" role="img" aria-label="Photo of a runner's foot on a dark track" style="background:linear-gradient(180deg,#1a1410,#6a3a20 60%,#2a2a2a)"></div><h3>Fuel Your Performance</h3></div>
  </div>
</section>

<section class="testimonials">
  <h2 class="section-title">Testimonials</h2>
  <div class="avatars">
    <svg class="chev" width="10" height="18" viewBox="0 0 10 18"><path d="M9 1 1 9l8 8" fill="none" stroke="#bbb" stroke-width="2"/></svg>
    <div class="avatar" role="img" aria-label="Portrait photo of a reviewer"></div>
    <div class="avatar" role="img" aria-label="Portrait photo of a reviewer" style="background:linear-gradient(180deg,#8a6a50,#3a2a20)"></div>
    <div class="avatar" role="img" aria-label="Portrait photo of a reviewer"></div>
    <svg class="chev" width="10" height="18" viewBox="0 0 10 18"><path d="M1 1l8 8-8 8" fill="none" stroke="#bbb" stroke-width="2"/></svg>
  </div>
  <blockquote class="quote">
    <span class="mark open">&ldquo;</span>
    Fusce condimentum, turpis ac placerat interdum, neque dolor viverra erat, id pulvinar ligula nulla eu urna. Vivamus vel molestie mi. Donec aliquam urna elit, vel molestie ipsum maximus rhoncus. Donec vitae neque et ex condimentum viverra tristique at metus. Curabitur sed consequat ipsum. Fusce eget tristique leo.
    <cite>Owen Hale, City</cite>
    <span class="mark close">&rdquo;</span>
  </blockquote>
</section>

<footer class="site-footer">
  <div class="wrap footer-grid">
    <ul class="footer-links"><li>Home</li><li>Water</li><li>Fruits &amp; Vegetables</li><li>Fuel your body</li></ul>
    <ul class="footer-links"><li>Drink more water</li><li>Fuel your performance</li><li>Stretch more</li><li>Protect your skin more</li></ul>
    <ul class="footer-links"><li>Move more</li><li>Sports mindset</li></ul>
    <div class="newsletter">
      <h4>Newsletter Subscribe</h4>
      <div class="subscribe"><span class="field">Email Address</span><span class="btn">SUBSCRIBE</span></div>
    </div>
    <div class="social">
      <h4>Social Media</h4>
      <div class="social-dots"><i></i><i></i><i style="background:#d0413a"></i><i style="background:#d0413a"></i></div>
    </div>
  </div>
</footer>
<div class="copyright">Copyright &copy; 2017 Company name. All rights reserved.</div>

</body>
</html>
```